Sticker Redesign

We provide document shredding services to clients. Clients are provided with shredding bins and employees/users of these companies dispose of unwanted confidential documents into these bins. Based on their schedule we come out and shred their documents in our specialty trucks and recycle the paper at the end of the day. We have our company decal on these bins which have a few objectives:
1. Motivate clients/users to dispose of all paper documents into our bins.
2. Instruct these clients/users on what can and CAN NOT go into our bins.
3. Brand our company
REDESIGN OBJECTIVES:
1. Our current label needs a redesign that will include items that cannot be placed into our bin as we have had an increase of items such as batteries and metal objects deposited into our bins. This leads to fires in our shredding trucks.
Allowed in Container: Paper Documents Only
Not Allowed in Container: All Other Waste; Batteries, Food, Metal, Electronics.
2. We also want to do a better job in educating clients/users to dispose of confidential documents into our bins and not garbage or recycling bins under their desks.
3. Modern, clean design look.
4. Size of label should remain the same.
Office employees

```html
<!DOCTYPE html>
<html lang="en">
<head>
<meta charset="utf-8">
<title>Mixed Paper &amp; Card Recycling Label</title>
<link rel="stylesheet" href="https://fonts.googleapis.com/css2?family=Ubuntu:wght@400;500;700&display=swap">
<style>
  :root {
    --sky: #1a9bd7;
    --sky-light: #43b0e2;
    --green: #22a94a;
    --red: #e5332a;
    --white: #ffffff;
    --ink: #111111;
  }
  html, body {
    margin: 0;
    padding: 0;
    width: 1200px;
    height: 223px;
    overflow: hidden;
    background: var(--white);
  }
  .label {
    position: relative;
    display: flex;
    width: 1200px;
    height: 223px;
    font-family: "Ubuntu", sans-serif;
    color: var(--white);
  }
  .hero {
    position: relative;
    width: 537px;
    height: 100%;
    background: var(--sky);
    overflow: hidden;
  }
  .hero__backdrop {
    position: absolute;
    inset: 0;
    background: radial-gradient(ellipse at 40% 45%, var(--sky-light) 0%, var(--sky) 70%);
  }
  .hero__icon {
    position: absolute;
    left: 218px;
    top: 36px;
    width: 84px;
    height: 78px;
  }
  .hero__title {
    position: absolute;
    left: 33px;
    top: 118px;
    margin: 0;
    font-size: 26px;
    font-weight: 500;
    letter-spacing: 0.2px;
    white-space: nowrap;
  }
  .hero__contact {
    position: absolute;
    left: 33px;
    right: 36px;
    top: 171px;
    display: flex;
    justify-content: space-between;
    font-size: 17px;
  }
  .rules {
    width: 195px;
    height: 100%;
    box-sizing: border-box;
    padding: 36px 0 0 34px;
  }
  .rules--yes { background: var(--green); }
  .rules--no { background: var(--red); width: 192px; padding-left: 28px; }
  .rules__heading {
    display: flex;
    align-items: center;
    gap: 6px;
    margin: 0 0 18px;
    font-size: 16px;
    font-weight: 700;
  }
  .rules__heading svg { width: 15px; height: 15px; }
  .rules__list {
    list-style: none;
    margin: 0;
    padding: 0;
    font-size: 17px;
    line-height: 25px;
  }
  .brand {
    flex: 1;
    background: var(--white);
    color: var(--ink);
    display: flex;
    flex-direction: column;
    align-items: center;
    justify-content: center;
  }
  .brand__row {
    display: flex;
    align-items: center;
    gap: 10px;
  }
  .brand__dot {
    width: 22px;
    height: 22px;
    border-radius: 50%;
    background: var(--sky);
  }
  .brand__name {
    font-size: 40px;
    font-weight: 700;
    color: var(--ink);
    letter-spacing: -0.5px;
  }
  .brand__tagline {
    margin-top: 14px;
    font-size: 18px;
    font-weight: 400;
  }
</style>
</head>
<body>
  <main class="label">
    <section class="hero">
      <div class="hero__backdrop" role="img" aria-label="Line drawings of scattered papers, newspapers, envelopes and boxes on blue"></div>
      <svg class="hero__icon" viewBox="0 0 84 78" aria-hidden="true">
        <g fill="none" stroke="var(--white)" stroke-width="10" stroke-linejoin="round">
          <path d="M30 28 L42 8 L54 28"/>
          <path d="M64 40 L76 62 L52 62"/>
          <path d="M34 62 L10 62 L22 40"/>
        </g>
        <g fill="var(--white)">
          <polygon points="56,18 70,24 60,34"/>
          <polygon points="40,54 48,68 40,72"/>
          <polygon points="16,30 26,20 30,34"/>
        </g>
      </svg>
      <h1 class="hero__title">MIXED PAPER &amp; CARD RECYCLING</h1>
      <div class="hero__contact">
        <span class="hero__web">www.northledger.ca</span>
        <span class="hero__phone">1-800-555-0142</span>
      </div>
    </section>

    <section class="rules rules--yes">
      <h2 class="rules__heading">YES PLEASE
        <svg viewBox="0 0 16 16" aria-hidden="true"><path d="M2 8.5 L6 12.5 L14 3.5" fill="none" stroke="var(--white)" stroke-width="3"/></svg>
      </h2>
      <ul class="rules__list">
        <li>Paper</li>
        <li>Magazines</li>
        <li>Newspapers</li>
        <li>Thin card</li>
        <li>Envelopes</li>
      </ul>
    </section>

    <section class="rules rules--no">
      <h2 class="rules__heading">NO THANKS
        <svg viewBox="0 0 16 16" aria-hidden="true"><path d="M3 3 L13 13 M13 3 L3 13" fill="none" stroke="var(--white)" stroke-width="3"/></svg>
      </h2>
      <ul class="rules__list">
        <li>All other waste</li>
        <li>Batteries</li>
        <li>Food</li>
        <li>Metal</li>
        <li>Electronics</li>
      </ul>
    </section>

    <section class="brand">
      <div class="brand__row">
        <span class="brand__dot" aria-hidden="true"></span>
        <span class="brand__name">Northledger</span>
      </div>
      <span class="brand__tagline">Information Security</span>
    </section>
  </main>
</body>
</html>
```